Bright Oak Fitness Facility Business Cards

Business Card Design that incorporates the logo and tagline

Target Market(s)

Fitness, People Who Exercise

Contact Information for Business Card

2817 Mossgrove Bend Road
Cedar Hollow, Florida 32190
Phone: 321-555-Jump (5867)
www.brightoakfitness.example
info@brightoakfitness.example

Requirements
Must have
• Logo, Address, Website, email and tagline "Strength For Life". Colors should be red/black/grey/white

```html
<!DOCTYPE html>
<html lang="en">
<head>
<meta charset="utf-8">
<title>Bright Oak Fitness – Business Cards</title>
<link href="https://fonts.googleapis.com/css2?family=Open+Sans:wght@400;700&display=swap" rel="stylesheet">
<style>
  :root {
    --backdrop: #d9d9d9;
    --card: #eeeeee;
    --red: #e52d3a;
    --deep-red: #7e0f16;
    --shade: #d2d2d2;
    --ink: #1a1a1a;
  }
  * { margin: 0; padding: 0; box-sizing: border-box; }
  html, body { width: 1200px; height: 864px; overflow: hidden; }
  body {
    background: var(--backdrop);
    font-family: "Open Sans", Arial, sans-serif;
    position: relative;
  }
  .card {
    position: absolute;
    width: 560px;
    height: 320px;
    background: var(--card);
    overflow: hidden;
    box-shadow: 0 10px 24px rgba(0,0,0,0.18);
  }
  .card--back { left: 580px; top: 70px; }
  .card--front { left: 60px; top: 470px; }
  .card__decor { position: absolute; inset: 0; width: 100%; height: 100%; }

  .brand {
    position: absolute;
    display: flex;
    align-items: center;
    gap: 10px;
  }
  .brand__mark { width: 18px; height: 18px; background: var(--red); }
  .brand__name {
    font-weight: 700;
    font-size: 26px;
    line-height: 34px;
    color: var(--ink);
    letter-spacing: 0.5px;
    white-space: nowrap;
  }
  .tagline {
    position: absolute;
    color: var(--red);
    font-size: 20px;
    line-height: 28px;
    white-space: nowrap;
  }
  .rule {
    position: absolute;
    height: 2px;
    background: var(--red);
  }

  /* back face */
  .card--back .brand { left: 125px; top: 104px; }
  .card--back .tagline { left: 0; right: 0; text-align: center; top: 152px; }
  .card--back .rule { left: 150px; top: 222px; width: 260px; }

  /* front face */
  .card--front .brand { left: 34px; top: 32px; }
  .card--front .tagline { left: 62px; top: 74px; }
  .contact {
    position: absolute;
    left: 34px;
    top: 122px;
    list-style: none;
  }
  .contact__item {
    display: flex;
    align-items: center;
    gap: 12px;
    font-size: 15px;
    line-height: 24px;
    color: var(--ink);
    white-space: nowrap;
  }
  .contact__item--cont { padding-left: 28px; }
  .contact__icon { width: 16px; height: 16px; flex: none; }
  .card--front .rule { left: 34px; top: 268px; width: 310px; }
</style>
</head>
<body>

  <section class="card card--back" aria-label="Card back">
    <svg class="card__decor" viewBox="0 0 560 320" aria-hidden="true">
      <polygon points="0,0 120,0 0,120" fill="var(--shade)"/>
      <polygon points="0,0 90,0 0,90" fill="var(--red)"/>
      <polygon points="0,0 40,0 0,40" fill="var(--deep-red)"/>
      <polygon points="560,140 560,320 380,320" fill="var(--shade)"/>
      <polygon points="560,170 560,320 410,320" fill="var(--red)"/>
      <polygon points="560,250 560,320 490,320" fill="var(--deep-red)"/>
    </svg>
    <div class="brand">
      <span class="brand__mark"></span>
      <span class="brand__name">BRIGHT OAK FITNESS</span>
    </div>
    <p class="tagline">Strength For Life</p>
    <div class="rule"></div>
  </section>

  <section class="card card--front" aria-label="Card front">
    <svg class="card__decor" viewBox="0 0 560 320" aria-hidden="true">
      <polygon points="560,120 560,320 360,320" fill="var(--shade)"/>
      <polygon points="560,150 560,320 390,320" fill="var(--red)"/>
      <polygon points="560,240 560,320 480,320" fill="var(--deep-red)"/>
    </svg>
    <div class="brand">
      <span class="brand__mark"></span>
      <span class="brand__name">BRIGHT OAK FITNESS</span>
    </div>
    <p class="tagline">Strength For Life</p>
    <ul class="contact">
      <li class="contact__item">
        <svg class="contact__icon" viewBox="0 0 16 16" aria-hidden="true"><rect width="16" height="16" rx="2" fill="var(--red)"/><path d="M5 3.5l2 2.2-1.2 1.3c.7 1.4 1.8 2.5 3.2 3.2l1.3-1.2 2.2 2-1.4 1.6C7.5 12.3 3.7 8.5 3.4 4.9z" fill="#fff"/></svg>
        321-555-Jump (5867)
      </li>
      <li class="contact__item">
        <svg class="contact__icon" viewBox="0 0 16 16" aria-hidden="true"><rect width="16" height="16" rx="2" fill="var(--red)"/><rect x="3" y="4.5" width="10" height="7" fill="none" stroke="#fff" stroke-width="1.3"/><path d="M3 4.5l5 4 5-4" fill="none" stroke="#fff" stroke-width="1.3"/></svg>
        info@brightoakfitness.example
      </li>
      <li class="contact__item">
        <svg class="contact__icon" viewBox="0 0 16 16" aria-hidden="true"><rect width="16" height="16" rx="2" fill="var(--red)"/><circle cx="8" cy="8" r="4.6" fill="none" stroke="#fff" stroke-width="1.2"/><path d="M3.4 8h9.2M8 3.4c-2 2.6-2 6.6 0 9.2M8 3.4c2 2.6 2 6.6 0 9.2" fill="none" stroke="#fff" stroke-width="1"/></svg>
        www.brightoakfitness.example
      </li>
      <li class="contact__item">
        <svg class="contact__icon" viewBox="0 0 16 16" aria-hidden="true"><rect width="16" height="16" rx="2" fill="var(--red)"/><path d="M8 13.5s-4-4-4-7a4 4 0 018 0c0 3-4 7-4 7z" fill="#fff"/><circle cx="8" cy="6.5" r="1.5" fill="var(--red)"/></svg>
        2817 Mossgrove Bend Road
      </li>
      <li class="contact__item contact__item--cont">Cedar Hollow, Florida 32190</li>
    </ul>
    <div class="rule"></div>
  </section>

</body>
</html>
```